design a catchy flyer for my electrical buisness

need a flyer designed to attract people to my business by looking professional and offering specials

Target Market(s)

all people i want to look affordable to everyone but still keeping that professional look and feel

Industry/Entity Type

Electrical

Requirements
Must have
• NO JOB TO BIG OR SMALL
• CALL NOW FOR A FREE QUOTE 0491570156
• NO CALL OUT FEE
• same promises as uploaded pic maybe written different style
• Your neighborhood electrician
• 100% satisfaction guaranteed
• were here to help
• mention this flyer for 10% off
• specializing in house renovations, extensions, kitchen and bathroom upgrades switchboard upgrades
• Make your house safe with our RCD and smoke alarm packages
Nice to have
• modern
• proffesional
• shows trust when customers read it
Should not have
• corny slogans
• cheap look

```html
<!DOCTYPE html>
<html lang="en">
<head>
<meta charset="UTF-8">
<title>VoltHaven – Your Neighbourhood Electrician</title>
<link href="https://fonts.googleapis.com/css2?family=Bebas+Neue&family=Questrial&family=Roboto+Condensed:ital,wght@0,300;0,400;1,400;1,700&display=swap" rel="stylesheet">
<style>
  :root {
    --orange: #f26a12;
    --orange-light: #f58a2a;
    --red: #f23a1f;
    --charcoal: #2d2d2d;
    --charcoal-soft: #3b3b3b;
    --grey: #4a4a4a;
    --paper: #f1f1f1;
    --white: #ffffff;
  }
  * { margin: 0; padding: 0; box-sizing: border-box; }
  html, body { width: 855px; height: 1200px; overflow: hidden; background: var(--paper); }
  .flyer { position: relative; width: 855px; height: 1200px; overflow: hidden; font-family: "Questrial", sans-serif; }
  .backdrop { position: absolute; inset: 0; }
  .abs { position: absolute; white-space: nowrap; }

  .tagline { left: 392px; top: 44px; font-size: 41px; color: #111; line-height: 1; }
  .trade { left: 394px; top: 90px; font-size: 81px; color: var(--orange); line-height: 1; }

  .guarantee-icon { left: 492px; top: 230px; width: 100px; height: 94px; border-radius: 10px; background: linear-gradient(#ffffff22, #ffffff10); border: 3px solid var(--white); }
  .guarantee-top { left: 606px; top: 244px; font-family: "Bebas Neue", sans-serif; font-size: 37px; color: var(--white); line-height: 1; }
  .guarantee-main { left: 606px; top: 276px; font-family: "Bebas Neue", sans-serif; font-size: 58px; color: var(--orange); line-height: 1; }

  .contact-label { left: 564px; top: 378px; font-size: 45px; color: var(--red); line-height: 1; }
  .contact-phone { left: 566px; top: 426px; font-size: 38px; color: var(--grey); line-height: 1; letter-spacing: 0.5px; }

  .brand { left: 44px; top: 434px; font-size: 62px; color: var(--white); line-height: 1; }

  .perks { left: 52px; top: 578px; list-style: none; }
  .perks li { position: relative; padding-left: 24px; font-size: 22px; color: #222; line-height: 1; margin-bottom: 19px; }
  .perks li::before { content: ""; position: absolute; left: 0; top: 4px; width: 12px; height: 12px; border-radius: 50%; background: var(--orange); }
  .perks li:nth-child(2) { margin-bottom: 15px; }

  .service { display: flex; align-items: center; justify-content: center; text-align: center; font-family: "Bebas Neue", sans-serif; color: var(--white); line-height: 0.95; }
  .service-fault { left: 539px; top: 485px; width: 248px; height: 248px; font-size: 54px; }
  .service-tv { left: 303px; top: 631px; width: 180px; height: 180px; font-size: 50px; }
  .service-led { left: 72px; top: 696px; width: 172px; height: 172px; font-size: 50px; }

  .offer { left: 545px; top: 770px; font-family: "Bebas Neue", sans-serif; font-size: 80px; color: var(--white); line-height: 1; }

  .headline { left: 34px; top: 888px; font-family: "Bebas Neue", sans-serif; font-size: 34px; color: var(--orange); line-height: 1; letter-spacing: 0.2px; }
  .specialties { left: 34px; top: 918px; font-family: "Bebas Neue", sans-serif; font-size: 22.5px; color: var(--white); line-height: 1; }

  .promise-title { left: 34px; top: 951px; font-family: "Roboto Condensed", sans-serif; font-style: italic; font-weight: 700; font-size: 21px; color: var(--orange); line-height: 1; }
  .promises { list-style: none; font-family: "Roboto Condensed", sans-serif; font-weight: 300; font-size: 17.5px; color: var(--white); }
  .promises li { position: relative; padding-left: 24px; height: 21.3px; line-height: 21px; }
  .promises li::before { content: ""; position: absolute; left: 3px; top: 6px; width: 10px; height: 10px; border-radius: 50%; background: var(--orange); }
  .promises sup { font-size: 10px; margin-left: 3px; }
  .promises-left { left: 38px; top: 978px; }
  .promises-right { left: 411px; top: 978px; }

  .footnotes { left: 36px; top: 1093px; font-family: "Roboto Condensed", sans-serif; font-style: italic; font-size: 13.8px; color: var(--white); line-height: 17px; }

  .licence { right: 47px; top: 1157px; font-size: 23px; color: var(--white); line-height: 1; }
</style>
</head>
<body>
<main class="flyer">
  <svg class="backdrop" width="855" height="1200" viewBox="0 0 855 1200" aria-hidden="true">
    <defs>
      <linearGradient id="paperShade" x1="0" y1="0" x2="1" y2="0">
        <stop offset="0" stop-color="#ffffff"/>
        <stop offset="1" stop-color="#dcdcdc"/>
      </linearGradient>
      <linearGradient id="orangeShade" x1="0" y1="0" x2="1" y2="1">
        <stop offset="0" stop-color="#ef5f0d"/>
        <stop offset="0.5" stop-color="#f58a2a"/>
        <stop offset="1" stop-color="#ee6410"/>
      </linearGradient>
      <linearGradient id="darkShade" x1="0" y1="0" x2="0" y2="1">
        <stop offset="0" stop-color="#3d3d3d"/>
        <stop offset="1" stop-color="#262626"/>
      </linearGradient>
    </defs>
    <rect width="855" height="1200" fill="url(#paperShade)"/>
    <!-- upper left orange field with dark edge -->
    <polygon points="268,0 300,0 575,502 548,502" fill="#3a3a3a"/>
    <polygon points="0,0 268,0 548,502 560,530 0,530" fill="url(#orangeShade)"/>
    <!-- guarantee band -->
    <polygon points="392,206 855,206 855,361 484,361" fill="var(--orange)"/>
    <polygon points="396,211 855,211 855,356 482,356" fill="#2e2e2e"/>
    <!-- divider under orange field -->
    <rect x="0" y="530" width="855" height="6" fill="#ffffff"/>
    <polygon points="0,536 560,536 545,546 0,548" fill="var(--orange)"/>
    <!-- lower dark field -->
    <polygon points="0,870 855,590 855,1200 0,1200" fill="url(#darkShade)"/>
    <!-- diagonal accents behind circles -->
    <polygon points="0,856 855,560 855,578 0,872" fill="var(--orange)"/>
    <polygon points="0,846 855,552 855,559 0,854" fill="#ffffff"/>
    <!-- service circles -->
    <circle cx="663" cy="609" r="134" fill="#ffffff"/>
    <circle cx="663" cy="609" r="124" fill="var(--red)"/>
    <circle cx="393" cy="721" r="99" fill="#ffffff"/>
    <circle cx="393" cy="721" r="90" fill="var(--red)"/>
    <circle cx="158" cy="782" r="95" fill="#ffffff"/>
    <circle cx="158" cy="782" r="86" fill="var(--red)"/>
    <!-- offer ribbon -->
    <polygon points="512,767 855,767 855,859 492,859" fill="url(#orangeShade)"/>
    <!-- footer -->
    <rect x="0" y="1139" width="855" height="6" fill="#ffffff"/>
    <rect x="0" y="1145" width="855" height="55" fill="url(#orangeShade)"/>
  </svg>

  <div class="abs tagline">Your Neighbourhood</div>
  <div class="abs trade">Electrician</div>

  <div class="abs guarantee-icon" role="img" aria-label="Thumbs-up icon"></div>
  <div class="abs guarantee-top">100% Satisfaction</div>
  <div class="abs guarantee-main">Guaranteed</div>

  <div class="abs contact-label">Contact us:</div>
  <div class="abs contact-phone">0491570156</div>

  <div class="abs brand">VoltHaven</div>

  <ul class="abs perks">
    <li>NO JOB TO BIG OR SMALL</li>
    <li>WERE HERE TO HELP</li>
    <li>NO CALL OUT FEE</li>
  </ul>

  <div class="abs service service-fault">General<br>Fault Fixing</div>
  <div class="abs service service-tv">TV and<br>Aerial</div>
  <div class="abs service service-led">L.E.D<br>Lights</div>

  <div class="abs offer">10% OFF</div>

  <div class="abs headline">Make your house safe with our RCD and smoke alarm packages</div>
  <div class="abs specialties">Specializing in house renovations, extensions, kitchen and bathroom upgrades switchboard upgrades</div>

  <div class="abs promise-title">OUR PROMISE TO YOU</div>
  <ul class="abs promises promises-left">
    <li>We will arrive on time or we will pay you $100<sup>1</sup></li>
    <li>Before any job begins you will know the exact cost</li>
    <li>We will provide you with a fixed price</li>
    <li>Guarantee assuring no extra costs</li>
    <li>We will leave your place as clean as when we arrived</li>
  </ul>
  <ul class="abs promises promises-right">
    <li>If there is a problem and it's our fault we will fix it for free</li>
    <li>We will return your telephone calls promptly</li>
    <li>We will provide a 12 Month warranty on all parts<sup>2</sup></li>
    <li>We will provide friendly, helpful service and advice</li>
  </ul>

  <div class="abs footnotes">
    1. if more than half and hour late from the scheduled time<br>
    2. 12 month warranty only applies to parts supplied and install by VOLTHAVEN.
  </div>

  <div class="abs licence">EC 048213</div>
</main>
</body>
</html>
```